Business Card Design Project

beauty / make up / lashes

Industry/Entity Type

Business

Contact Information for Business Card

pink / gold / wait / black vintage classic elegant design

```html
<!DOCTYPE html>
<html lang="en">
<head>
<meta charset="utf-8">
<title>mira lashes – business card</title>
<link href="https://fonts.googleapis.com/css2?family=Questrial&display=swap" rel="stylesheet">
<style>
  :root {
    --page: #e9e6e4;
    --card: #1b1a1b;
    --deco: #35222f;
    --deco-ring: #262524;
    --pink: #e5168c;
    --gold: #d7a93c;
    --text: #f4f1f3;
  }
  * { box-sizing: border-box; margin: 0; padding: 0; }
  html, body { width: 1200px; height: 784px; overflow: hidden; }
  body {
    background: var(--page);
    font-family: "Questrial", "Century Gothic", sans-serif;
    display: flex;
    align-items: center;
    justify-content: center;
    gap: 40px;
  }
  .card {
    position: relative;
    width: 540px;
    height: 310px;
    background: var(--card);
    overflow: hidden;
    border-radius: 3px;
    box-shadow: 0 6px 18px rgba(0,0,0,.18);
  }
  .card__deco {
    position: absolute;
    width: 360px;
    height: 360px;
    border-radius: 50%;
    background: var(--deco);
    border: 26px solid var(--deco-ring);
  }
  .card--back .card__deco { left: -150px; top: -40px; }
  .card--front .card__deco { right: -160px; top: -30px; }

  .brand {
    position: absolute;
    display: flex;
    align-items: center;
    gap: 12px;
  }
  .brand__dot {
    width: 46px; height: 46px;
    border-radius: 50%;
    background: var(--pink);
  }
  .brand__name {
    color: var(--gold);
    font-size: 34px;
    letter-spacing: .5px;
  }
  .card--back .brand { left: 190px; top: 60px; }
  .card--front .brand { left: 60px; top: 70px; }

  .contact {
    position: absolute;
    left: 60px;
    bottom: 32px;
    list-style: none;
    color: var(--text);
    font-size: 14.5px;
    line-height: 20px;
  }
  .contact li { display: flex; align-items: center; gap: 8px; }
  .contact svg { width: 14px; height: 14px; fill: var(--pink); flex: none; }
</style>
</head>
<body>

  <section class="card card--back" aria-label="Card back">
    <div class="card__deco" aria-hidden="true"></div>
    <div class="brand">
      <span class="brand__dot"></span>
      <span class="brand__name">mira lashes</span>
    </div>
  </section>

  <section class="card card--front" aria-label="Card front">
    <div class="card__deco" aria-hidden="true"></div>
    <div class="brand">
      <span class="brand__dot"></span>
      <span class="brand__name">mira lashes</span>
    </div>
    <ul class="contact">
      <li>
        <svg viewBox="0 0 14 14" aria-hidden="true"><path d="M4 0h6a1 1 0 0 1 1 1v12a1 1 0 0 1-1 1H4a1 1 0 0 1-1-1V1a1 1 0 0 1 1-1zm0 2v9h6V2z"/></svg>
        555 201 4870
      </li>
      <li>
        <svg viewBox="0 0 14 14" aria-hidden="true"><path d="M3 1l2.5 3-1.5 1.5c.8 1.8 2.2 3.2 4 4L9.5 8l3 2.5-1.5 2.5C6 13 1 8 .5 3z"/></svg>
        555 309 2264
      </li>
      <li>
        <svg viewBox="0 0 14 14" aria-hidden="true"><path d="M0 3h14v9H0zm1.5 1.2V5l5.5 3.5L12.5 5v-.8L7 7.5z"/></svg>
        hello@miralashstudio.com
      </li>
      <li>
        <svg viewBox="0 0 14 14" aria-hidden="true"><path d="M7 0a7 7 0 1 0 0 14A7 7 0 0 0 7 0zm0 1.5c.9.9 1.5 2.8 1.6 4.7H5.4C5.5 4.3 6.1 2.4 7 1.5zM1.6 6.2A5.5 5.5 0 0 1 4.4 2 9 9 0 0 0 3.9 6.2zm8.5 0A9 9 0 0 0 9.6 2a5.5 5.5 0 0 1 2.8 4.2zM1.6 7.8h2.3A9 9 0 0 0 4.4 12a5.5 5.5 0 0 1-2.8-4.2zm3.8 0h3.2c-.1 1.9-.7 3.8-1.6 4.7-.9-.9-1.5-2.8-1.6-4.7zm4.7 0h2.3A5.5 5.5 0 0 1 9.6 12a9 9 0 0 0 .5-4.2z"/></svg>
        www.miralashstudio.com
      </li>
      <li>
        <svg viewBox="0 0 14 14" aria-hidden="true"><path d="M7 1l7 6h-2v6H8.5V9h-3v4H2V7H0z"/></svg>
        18 Elm Grove Lane, R D 4, Fairview 0417
      </li>
    </ul>
  </section>

</body>
</html>
```